illustration of crowdfunding universe

I need a diagram to include on my website and i presentations, etc.
The diagram needs to depict the various types of 'crowdfunding' options that are available in the U.S to companies and people in the U.S.
I've attached a very rough hand sketch of my idea bu am open to suggestions
A mockup of my website can be found here: http://shortlinkly.example/kq7vzt4
The illustration should match the 'theme' of the website
I expect that there will be a number of iterations but I plan to pick someone to help me with the illustration very quickly.
Thanks
Industry/Entity Type
Crowdfunding
Look and feel
Each slider illustrates characteristics of the customer's brand and the style your logo design should communicate.

```html
<!DOCTYPE html>
<html lang="en">
<head>
<meta charset="utf-8">
<title>Crowdfunding Universe</title>
<link rel="stylesheet" href="https://fonts.googleapis.com/css2?family=Poiret+One&display=swap">
<style>
  :root {
    --page: #ffffff;
    --universe: #e2f6cc;
    --ring: #3f8f2a;
    --node-light: #a6f25a;
    --node-dark: #3cc41c;
    --node-edge: #2f7f1f;
    --ink: #333333;
    --flow: #55b52b;
    --bullet: #6cc84a;
    --figure: #2f6e22;
  }
  html, body { margin: 0; padding: 0; overflow: hidden; background: var(--page); }
  .canvas { width: 1200px; height: 1062px; position: relative; }
  .diagram { display: block; width: 1200px; height: 1062px; font-family: "Poiret One", sans-serif; }
  .universe { fill: var(--universe); }
  .orbit { fill: none; stroke: var(--ring); stroke-width: 1.6; stroke-dasharray: 6 5; }
  .node { fill: url(#nodeFill); stroke: var(--node-edge); stroke-width: 1.4; stroke-dasharray: 4 3; }
  .node-label { fill: var(--ink); font-size: 13px; text-anchor: middle; }
  .node-label.compact { font-size: 12px; }
  .node-label .small { font-size: 9px; }
  .flow { fill: none; stroke: var(--ring); stroke-width: 1.5; stroke-dasharray: 5 4; }
  .flow-label { fill: var(--flow); font-size: 15px; text-anchor: middle; }
  .flow-label .small { font-size: 10px; }
  .money { fill: var(--ink); font-size: 22px; text-anchor: middle; font-weight: 700; }
  .note text { fill: var(--ink); font-size: 12.5px; paint-order: stroke; stroke: var(--universe); stroke-width: 4px; stroke-linejoin: round; }
  .note .dot { fill: var(--bullet); }
  .crowd-figures { fill: var(--figure); opacity: .55; }
</style>
</head>
<body>
<div class="canvas">
<svg class="diagram" viewBox="0 0 1024 906" xmlns="http://www.w3.org/2000/svg" role="img" aria-label="Crowdfunding universe diagram">
  <defs>
    <radialGradient id="nodeFill" cx="40%" cy="35%" r="70%">
      <stop offset="0" stop-color="#a6f25a"/>
      <stop offset="1" stop-color="#3cc41c"/>
    </radialGradient>
    <marker id="arrowHead" viewBox="0 0 10 10" refX="9" refY="5" markerWidth="7" markerHeight="7" orient="auto-start-reverse">
      <path d="M0 0 L10 5 L0 10 z" fill="#3f8f2a"/>
    </marker>
  </defs>

  <ellipse class="universe" cx="512" cy="455" rx="488" ry="426"/>
  <ellipse class="orbit" cx="511" cy="469" rx="290" ry="321"/>

  <line class="flow" x1="487" y1="386" x2="489" y2="245" marker-start="url(#arrowHead)" marker-end="url(#arrowHead)"/>
  <line class="flow" x1="330" y1="342" x2="445" y2="415" marker-start="url(#arrowHead)"/>
  <line class="flow" x1="340" y1="352" x2="450" y2="425" marker-end="url(#arrowHead)"/>
  <line class="flow" x1="580" y1="455" x2="695" y2="375" marker-end="url(#arrowHead)"/>
  <line class="flow" x1="692" y1="388" x2="585" y2="462" marker-end="url(#arrowHead)"/>
  <line class="flow" x1="460" y1="478" x2="370" y2="565" marker-end="url(#arrowHead)"/>
  <line class="flow" x1="572" y1="522" x2="628" y2="602" marker-start="url(#arrowHead)"/>
  <line class="flow" x1="582" y1="515" x2="638" y2="596" marker-end="url(#arrowHead)"/>

  <text class="money" x="471" y="328">$$</text>
  <text class="flow-label" x="524" y="307">EQUITY</text>
  <text class="flow-label" x="524" y="330"><tspan class="small">OR</tspan>LOAN</text>
  <text class="money" x="359" y="402" transform="rotate(-20 359 402)">$$</text>
  <g transform="rotate(-55 395 330)">
    <text class="flow-label" x="395" y="318">REWARDS</text>
    <text class="flow-label" x="395" y="338"><tspan class="small">OR</tspan> GOODS</text>
    <text class="flow-label" x="395" y="358"><tspan class="small">OR</tspan> DONATION</text>
  </g>
  <g transform="rotate(-35 597 410)">
    <text class="flow-label" x="597" y="402">EQUITY</text>
    <text class="flow-label" x="597" y="421"><tspan class="small">OR</tspan>LOAN</text>
  </g>
  <g transform="rotate(-35 652 450)">
    <text class="flow-label" x="652" y="440">ACCREDITED</text>
    <text class="flow-label" x="652" y="460">INVESTORS</text>
  </g>
  <text class="money" x="394" y="518">$$</text>
  <text class="flow-label" x="435" y="546">LOAN</text>
  <text class="money" x="578" y="588" transform="rotate(-20 578 588)">$$</text>
  <text class="flow-label" x="632" y="560" transform="rotate(-55 632 560)">LOAN</text>

  <circle class="node" cx="490" cy="200" r="40"/>
  <text class="node-label" x="490" y="199">COMPANY</text>
  <text class="node-label" x="490" y="216">1</text>

  <circle class="node" cx="290" cy="322" r="40"/>
  <text class="node-label" x="290" y="320">COMPANY</text>
  <text class="node-label" x="290" y="337"><tspan class="small">OR</tspan> PEOPLE</text>

  <circle class="node" cx="735" cy="357" r="40"/>
  <text class="node-label" x="735" y="360">COMPANY</text>
  <text class="node-label" x="735" y="377">2</text>

  <circle class="node" cx="337" cy="597" r="38"/>
  <text class="node-label" x="337" y="602">PEOPLE</text>

  <circle class="node" cx="657" cy="637" r="40"/>
  <text class="node-label compact" x="657" y="642">COMPANIES</text>

  <circle class="node" cx="487" cy="430" r="42"/>
  <text class="node-label" x="487" y="420">CROWD</text>
  <rect class="crowd-figures" x="464" y="428" width="46" height="30" rx="6" role="img" aria-label="Three small crowd figures"/>

  <circle class="node" cx="540" cy="476" r="45"/>
  <rect class="crowd-figures" x="514" y="462" width="52" height="34" rx="6" role="img" aria-label="Three small crowd figures"/>

  <g class="note">
    <circle class="dot" cx="434" cy="58" r="2"/><text x="439" y="62">CFHQ Can Help</text>
    <circle class="dot" cx="434" cy="77" r="2"/><text x="439" y="81">Loading to raise &lt;/ 12 Months</text>
    <circle class="dot" cx="434" cy="96" r="2"/><text x="439" y="100">Referred to as JOBS ACT card Funding</text>
    <circle class="dot" cx="434" cy="115" r="2"/><text x="439" y="119">SEC specific Funding</text>
    <circle class="dot" cx="434" cy="134" r="2"/><text x="439" y="138">NOT YET LEGAL</text>
  </g>
  <g class="note">
    <circle class="dot" cx="101" cy="236" r="2"/><text x="106" y="240">Anyone can give Money</text>
    <circle class="dot" cx="101" cy="257" r="2"/><text x="106" y="261">Typically used to support</text>
    <text x="106" y="282">different causes or</text>
    <text x="106" y="303">not-for-profit ventures</text>
    <circle class="dot" cx="101" cy="320" r="2"/><text x="106" y="324">Eg Backerly, Givio60</text>
  </g>
  <g class="note">
    <circle class="dot" cx="796" cy="332" r="2"/><text x="801" y="336">Only AI Can</text>
    <circle class="dot" cx="796" cy="353" r="2"/><text x="801" y="357">No Limit on Amount to Raise</text>
    <circle class="dot" cx="796" cy="374" r="2"/><text x="801" y="378">REG D or Rule 506,</text>
    <circle class="dot" cx="796" cy="395" r="2"/><text x="801" y="399">Crowd Funding</text>
    <circle class="dot" cx="796" cy="416" r="2"/><text x="801" y="420">Eg  seedcircle.example</text>
    <text x="822" y="441">growthround.example</text>
  </g>
  <g class="note">
    <circle class="dot" cx="121" cy="594" r="2"/><text x="127" y="598">Anyone can lend</text>
    <circle class="dot" cx="121" cy="615" r="2"/><text x="127" y="619">Website vets potential</text>
    <text x="127" y="640">borrowers</text>
    <circle class="dot" cx="121" cy="657" r="2"/><text x="127" y="661">Commonly known as</text>
    <text x="127" y="682">peek to peek lending (P2P)</text>
    <text x="127" y="703">Eg Backerly, Givio60</text>
  </g>
  <g class="note">
    <circle class="dot" cx="689" cy="684" r="2"/><text x="694" y="688">Website reviews companies</text>
    <text x="694" y="709">that want to borrow</text>
    <circle class="dot" cx="689" cy="726" r="2"/><text x="694" y="730">Only AI can invest</text>
    <circle class="dot" cx="689" cy="747" r="2"/><text x="694" y="751">eg, LendRing USA</text>
  </g>
</svg>
</div>
</body>
</html>
```